ROLL-ON-VERANDA Business Card Design

Please do not submit more than one design per designer. Both the front and the back must be submitted as a single design. Please use all of the attached files to design a two-sided business card. Do not use tiny text that is hard to read. Do not put text or images too close to the edges where it might get cut off during printing. The card should be horizontal. Please do not send me the same design that I attached showing the business information. Be creative.

One file is marked as the primary logo for company. Other files are marked as secondary. All logos should be incorporated into the design with a focus on the primary one being bigger.

```html
<!DOCTYPE html>
<html lang="en">
<head>
<meta charset="utf-8">
<title>ROLL-ON-VERANDA Business Card</title>
<link rel="stylesheet" href="https://fonts.googleapis.com/css2?family=Russo+One&family=Montserrat:wght@400;500&display=swap">
<style>
  :root{
    --navy:#12144a;
    --navy-band:#24317a;
    --gold:#f8c232;
    --red:#e41e2d;
    --grey:#6b6f86;
    --white:#ffffff;
    --badge-blue:#2f5ea8;
    --backdrop:#3a3a3c;
  }
  *{box-sizing:border-box;margin:0;padding:0}
  html,body{width:1200px;height:900px;overflow:hidden;background:var(--backdrop)}
  .stage{position:relative;width:1200px;height:900px}
  .card{position:absolute;width:700px;height:400px;border-radius:22px;background:var(--navy);overflow:hidden;color:var(--white);box-shadow:0 14px 30px rgba(0,0,0,.45)}
  .card--front{left:70px;top:40px}
  .card--back{left:430px;top:465px}

  .boat-art{position:absolute;background:linear-gradient(160deg,#e9ebf5,#8f94b8);border-radius:40% 60% 30% 50%/50% 50% 40% 40%;opacity:.9}
  .card--front .boat-art{left:240px;top:48px;width:220px;height:110px}
  .card--back .boat-art{left:500px;top:34px;width:140px;height:70px}

  .wordmark{font-family:"Russo One",sans-serif;color:var(--white);letter-spacing:1px;position:absolute;white-space:nowrap}
  .card--front .wordmark{left:0;right:0;top:178px;text-align:center;font-size:46px}
  .card--back .wordmark{left:450px;width:240px;top:114px;text-align:center;font-size:22px}

  .tagline{position:absolute;left:30px;right:30px;top:270px;text-align:center;font-family:"Russo One",sans-serif;font-size:16px;line-height:1.6;letter-spacing:.5px;white-space:nowrap}
  .tagline .highlight{color:var(--gold)}

  .swoosh{position:absolute;inset:0}
  .person{position:absolute;left:36px;top:40px}
  .person__name{font-family:"Russo One",sans-serif;color:var(--gold);font-size:25px;letter-spacing:.5px;white-space:nowrap}
  .person__creds{font-family:"Montserrat",sans-serif;font-size:17px;line-height:1.4;margin-top:8px}

  .contacts{position:absolute;left:0;top:228px;width:380px;list-style:none}
  .contacts li{display:flex;align-items:center;gap:14px;height:34px;margin-bottom:6px;padding-left:36px;font-family:"Montserrat",sans-serif;font-size:17px;white-space:nowrap;background:linear-gradient(90deg,var(--navy-band) 55%,rgba(36,49,122,0))}
  .contacts .icon{width:26px;height:26px;border-radius:50%;background:var(--gold);display:flex;align-items:center;justify-content:center;flex:none}
  .contacts .note{color:var(--gold);font-size:12px;margin-left:4px}

  .badge{position:absolute;width:52px;height:52px;border-radius:50%}
  .badge--anchor{left:444px;top:320px;background:var(--navy);border:3px solid var(--gold)}
  .badge--veteran{left:516px;top:290px;background:var(--red)}
  .badge--guard{left:588px;top:256px;background:var(--navy)}
  .badge--council{left:640px;top:214px;background:var(--badge-blue)}
</style>
</head>
<body>
<main class="stage">

  <section class="card card--front" aria-label="Card front">
    <div class="boat-art" role="img" aria-label="White line illustration of a cabin motor boat"></div>
    <div class="wordmark">ROLL-ON-VERANDA</div>
    <p class="tagline">PROVIDING <span class="highlight">HANDS-ON BOAT TRAINING</span>, CAPTAINING SERVICES<br>AND DELIVERIES IN THE HARBOR COUNTY AREA.</p>
  </section>

  <section class="card card--back" aria-label="Card back">
    <svg class="swoosh" width="700" height="400" viewBox="0 0 700 400" aria-hidden="true">
      <path d="M110 400 C330 385 560 300 700 185 L700 400 Z" fill="var(--white)"/>
      <path d="M100 392 C330 375 560 290 700 172" fill="none" stroke="var(--gold)" stroke-width="12"/>
      <path d="M140 380 C350 362 560 280 700 160" fill="none" stroke="var(--grey)" stroke-width="5" opacity=".7"/>
      <path d="M430 318 C540 280 630 225 700 168" fill="none" stroke="var(--red)" stroke-width="6"/>
      <path d="M120 400 C340 388 565 305 700 190" fill="none" stroke="var(--navy)" stroke-width="4"/>
    </svg>

    <div class="boat-art" role="img" aria-label="White line illustration of a cabin motor boat"></div>
    <div class="wordmark">ROLL-ON-VERANDA</div>

    <div class="person">
      <h1 class="person__name">CAPTAIN DORIAN K. HALVERS</h1>
      <p class="person__creds">USCG Licensed Master Captain<br>NBC Certified Instructor<br>Graduate Degree<br>Veteran</p>
    </div>

    <ul class="contacts">
      <li><span class="icon"><svg width="14" height="14" viewBox="0 0 24 24"><path d="M6.6 10.8a15 15 0 0 0 6.6 6.6l2.2-2.2c.3-.3.7-.4 1-.2 1.1.4 2.3.6 3.6.6.6 0 1 .4 1 1V20c0 .6-.4 1-1 1A17 17 0 0 1 3 4c0-.6.4-1 1-1h3.5c.6 0 1 .4 1 1 0 1.3.2 2.5.6 3.6.1.3 0 .7-.2 1z" fill="var(--navy)"/></svg></span>(555)340-2718<span class="note">(Text)</span></li>
      <li><span class="icon"><svg width="14" height="14" viewBox="0 0 24 24"><path d="M3 6h18v12H3z" fill="var(--navy)"/><path d="M3 6l9 7 9-7" fill="none" stroke="var(--gold)" stroke-width="2"/></svg></span>service@rollonveranda.com</li>
      <li><span class="icon"><svg width="14" height="14" viewBox="0 0 24 24"><circle cx="12" cy="12" r="9" fill="var(--navy)"/><path d="M3 12h18M12 3c3 3 3 15 0 18M12 3c-3 3-3 15 0 18" fill="none" stroke="var(--gold)" stroke-width="1.4"/></svg></span>www.Roll-On-Veranda.com</li>
    </ul>

    <div aria-label="Certification badges">
      <span class="badge badge--anchor"></span>
      <span class="badge badge--veteran"></span>
      <span class="badge badge--guard"></span>
      <span class="badge badge--council"></span>
    </div>
  </section>

</main>
</body>
</html>
```